Design for an iOS and Android app managing shopping list

The app allows you to keep manage shopping lists, each shopping list being made of items to buy...
We need a design for the 3 screens of the app:
a) global view showing list of (shopping) list
b) form enabling to edit the name of a (shopping) list
c) detailed view listing the contents/items of a (shopping) list
d) 1 text page [not illustrated]
2 "alerts" items are also to be designed: confirm and error pop ups.
No specific guidelines, nor logo or whatever.
It will be a free app distributed on iOS and Androïd.
We just want to make it looking nice & very usable for end users.

```html
<!DOCTYPE html>
<html lang="en">
<head>
<meta charset="utf-8">
<title>Update List Name Screen</title>
<link rel="stylesheet" href="https://fonts.googleapis.com/css2?family=Lato:wght@300&family=Open+Sans:wght@400;600;700&display=swap">
<style>
  :root {
    --backdrop: #f44d3a;
    --status-bar: #e2412f;
    --app-bar: #f14a37;
    --screen-bg: #f0f0f0;
    --panel: #ffffff;
    --ink: #222222;
    --rule: #c8c8c8;
    --white: #ffffff;
    --save: #20d89b;
    --save-edge: #17b07d;
  }
  * { box-sizing: border-box; margin: 0; padding: 0; }
  html, body { width: 1200px; height: 675px; overflow: hidden; }
  body {
    background: var(--backdrop);
    font-family: "Open Sans", Arial, sans-serif;
    position: relative;
  }
  .app-screen {
    position: absolute;
    left: 133px; top: 175px;
    width: 279px; height: 500px;
    background: var(--screen-bg);
    overflow: hidden;
  }
  .status-bar {
    height: 15px;
    background: var(--status-bar);
    color: var(--white);
    font-size: 7px;
    font-weight: 700;
    display: flex; align-items: center; justify-content: space-between;
    padding: 0 5px;
    position: relative;
  }
  .status-left, .status-right { display: flex; align-items: center; gap: 3px; }
  .status-time { position: absolute; left: 50%; transform: translateX(-50%); }
  .app-bar {
    height: 44px;
    background: var(--app-bar);
    color: var(--white);
    display: flex; align-items: center; justify-content: center;
    position: relative;
  }
  .app-title {
    font-size: 15.5px; font-weight: 700; letter-spacing: -0.2px;
    display: flex; align-items: center; gap: 6px;
  }
  .basket-icon { position: absolute; right: 10px; top: 12px; }
  .name-panel {
    background: var(--panel);
    height: 53px;
    padding: 15px 18px 0 17px;
    border-bottom: 1px solid #e6e6e6;
  }
  .name-field {
    font-size: 13.5px;
    color: var(--ink);
    border-bottom: 1.5px solid var(--rule);
    padding-bottom: 2px;
    display: flex; align-items: center;
  }
  .caret { display: inline-block; width: 1px; height: 14px; background: var(--ink); margin-left: 1px; }
  .save-button {
    position: absolute;
    left: 7px; top: 443px;
    width: 265px; height: 43px;
    background: var(--save);
    border-bottom: 3px solid var(--save-edge);
    border-radius: 2px;
    color: var(--white);
    font-size: 20px; font-weight: 700;
    display: flex; align-items: center; justify-content: center;
  }
  .caption {
    position: absolute;
    left: 486px; top: 356px;
    color: var(--white);
    font-family: "Lato", Arial, sans-serif;
    font-weight: 300;
    font-size: 32px;
    letter-spacing: 0.3px;
  }
</style>
</head>
<body>
  <main class="app-screen">
    <div class="status-bar">
      <div class="status-left">
        <svg width="11" height="6" viewBox="0 0 11 6" aria-hidden="true">
          <rect x="0" y="4" width="1.5" height="2" fill="#fff"/>
          <rect x="2.2" y="3" width="1.5" height="3" fill="#fff"/>
          <rect x="4.4" y="2" width="1.5" height="4" fill="#fff"/>
          <rect x="6.6" y="1" width="1.5" height="5" fill="#fff"/>
          <rect x="8.8" y="0" width="1.5" height="6" fill="#fff"/>
        </svg>
        <span>KL CZ</span>
        <svg width="10" height="7" viewBox="0 0 10 7" aria-hidden="true">
          <path d="M1 2.5 A6 6 0 0 1 9 2.5" stroke="#fff" stroke-width="1.2" fill="none"/>
          <path d="M2.6 4 A3.6 3.6 0 0 1 7.4 4" stroke="#fff" stroke-width="1.2" fill="none"/>
          <circle cx="5" cy="6" r="1" fill="#fff"/>
        </svg>
      </div>
      <span class="status-time">2:49 PM</span>
      <div class="status-right">
        <svg width="8" height="8" viewBox="0 0 8 8" aria-hidden="true">
          <circle cx="4" cy="4" r="3.3" stroke="#fff" stroke-width="1" fill="none"/>
          <rect x="2.6" y="3.6" width="2.8" height="2" fill="#fff"/>
          <path d="M3 3.6 V3 a1 1 0 0 1 2 0 V3.6" stroke="#fff" stroke-width="0.7" fill="none"/>
        </svg>
        <span>41 %</span>
        <svg width="15" height="7" viewBox="0 0 15 7" aria-hidden="true">
          <rect x="0.5" y="0.5" width="12" height="6" rx="1" stroke="#fff" fill="none"/>
          <rect x="2" y="2" width="4.2" height="3" fill="#fff"/>
          <rect x="13" y="2.3" width="1.3" height="2.4" fill="#fff"/>
        </svg>
      </div>
    </div>

    <header class="app-bar">
      <h1 class="app-title">
        <svg width="17" height="17" viewBox="0 0 17 17" aria-hidden="true">
          <path d="M3 14 L4 10 L12 2 L15 5 L7 13 Z" stroke="#fff" stroke-width="1.6" fill="none" stroke-linejoin="round"/>
          <path d="M10.5 3.5 L13.5 6.5" stroke="#fff" stroke-width="1.4"/>
          <path d="M4 10 L7 13" stroke="#fff" stroke-width="1.2"/>
        </svg>
        UPDATE LIST NAME
      </h1>
      <svg class="basket-icon" width="21" height="19" viewBox="0 0 21 19" aria-hidden="true">
        <path d="M6 7 L10.5 1.5 L15 7" stroke="#fff" stroke-width="1.6" fill="none" stroke-linecap="round"/>
        <path d="M1 7 H20 L18 17.5 H3 Z" stroke="#fff" stroke-width="1.6" fill="none" stroke-linejoin="round"/>
        <path d="M7 10 V15 M10.5 10 V15 M14 10 V15" stroke="#fff" stroke-width="1.4"/>
      </svg>
    </header>

    <section class="name-panel">
      <div class="name-field">Diner de ce soir<span class="caret"></span></div>
    </section>

    <div class="save-button">SAVE</div>
  </main>

  <p class="caption">Screen for Updating a Shopping List Name</p>
</body>
</html>
```